Business Cards,Stationary, HTML e-mail template
New Employee Benefits Business
Business Cards,Stationary, HTML e-mail template -
Creative Brief
Professional
Peter L. Marsh GBDS
Chief Benefits Guru
Suite 410 27 Kestrel Lane Webster, NY 14580
PMarsh@HarborlineWorkforce.com
www.HarborlineWorkforce.com
"Paperless" Open Enrollment Customize a 3-year Benefits Vision Survive a DOL Investigation Implement HR Services Portal

```html
<!DOCTYPE html>
<html lang="en">
<head>
<meta charset="utf-8">
<title>Harborline Workforce Stationery</title>
<link href="https://fonts.googleapis.com/css2?family=Arimo:wght@400;700&display=swap" rel="stylesheet">
<style>
:root{
  --backdrop:#8a4a22;
  --navy:#1d3690;
  --navy-deep:#14246a;
  --blue-light:#4f6fcf;
  --orange:#e8912b;
  --orange-light:#f3b865;
  --paper:#ffffff;
  --ink:#4a4a4a;
  --grey:#c9cbd0;
  --grey-light:#eef0f3;
}
*{box-sizing:border-box;margin:0;padding:0}
html,body{width:1200px;height:780px;overflow:hidden}
body{background:var(--backdrop);font-family:"Arimo",Arial,sans-serif;color:var(--ink);position:relative}
.piece{position:absolute;background:var(--paper);box-shadow:0 3px 8px rgba(0,0,0,.35);overflow:hidden}

.brand{display:flex;align-items:center;gap:4px;color:var(--navy);font-weight:700;line-height:1;white-space:nowrap}
.brand-dot{border-radius:50%;background:var(--orange);flex:none}

/* business card fronts */
.card{width:137px;height:72px}
.card-band{position:absolute;left:0;right:0;height:34px;padding:6px 8px;text-align:right;color:#fff}
.band-blue{top:0;background:linear-gradient(90deg,var(--navy-deep),var(--blue-light))}
.band-orange{bottom:0;top:auto;background:linear-gradient(90deg,var(--orange),var(--orange-light))}
.card-name{font-size:6.5px;font-weight:700}
.card-title{font-size:5px;margin-top:2px}
.card .brand{position:absolute;font-size:8px}
.card .brand-dot{width:10px;height:10px}

/* business card backs */
.card-back{width:139px;height:72px;padding:10px}
.card-back .brand{font-size:7px;justify-content:center}
.card-back .brand-dot{width:10px;height:10px}
.services{margin-top:6px;font-size:4.5px;line-height:1.45;text-align:center;color:var(--ink)}

/* letterhead */
.letterhead{left:377px;top:149px;width:348px;height:487px}
.letterhead .brand{position:absolute;left:14px;top:14px;font-size:12px}
.letterhead .brand-dot{width:16px;height:16px}
.faint-mark{position:absolute;left:124px;top:186px;width:100px;height:100px;border-radius:50%;background:radial-gradient(circle,rgba(232,145,43,.14),rgba(29,54,144,.08))}
.lh-footer{position:absolute;left:0;right:0;bottom:22px;text-align:center;font-size:6px;line-height:1.6}
.lh-bar{position:absolute;left:0;right:0;bottom:0;height:14px;background:linear-gradient(90deg,var(--navy-deep),var(--blue-light));color:#fff;font-size:5.5px;text-align:center;line-height:14px}

/* envelopes */
.envelope{left:749px;width:422px}
.env-back{top:43px;height:307px}
.env-front{top:389px;height:343px}
.envelope .brand.corner{position:absolute;left:10px;top:10px;font-size:11px}
.envelope .brand-dot{width:15px;height:15px}
.env-address{position:absolute;left:0;right:0;text-align:center;font-size:6px;line-height:1.6}
.env-web{position:absolute;left:0;right:0;text-align:center;font-size:6px;color:var(--ink)}
.env-flap{position:absolute;left:0;top:150px;width:422px;height:157px}
.env-flap .brand{position:absolute;left:50%;top:26px;transform:translateX(-50%);font-size:12px}
.env-band{position:absolute;left:0;right:0;height:20px;background:linear-gradient(90deg,var(--navy-deep),var(--blue-light));color:#fff;font-size:6px;text-align:center;line-height:20px}
</style>
</head>
<body>

<!-- business card fronts -->
<div class="piece card" style="left:79px;top:259px">
  <div class="card-band band-blue"><div class="card-name">Peter L. Marsh GBDS</div><div class="card-title">Chief Benefits Guru</div></div>
  <div class="brand" style="left:8px;top:46px"><span class="brand-dot"></span>HARBORLINE</div>
</div>
<div class="piece card" style="left:79px;top:348px">
  <div class="card-band" style="top:0;height:34px;color:var(--navy)"><div class="card-name">Peter L. Marsh GBDS</div><div class="card-title">Chief Benefits Guru</div></div>
  <div class="brand" style="left:8px;top:20px"><span class="brand-dot"></span>HARBORLINE</div>
  <div class="card-band band-orange" style="height:24px"></div>
</div>
<div class="piece card" style="left:79px;top:434px">
  <div class="card-band band-blue"><div class="card-name">Peter L. Marsh GBDS</div><div class="card-title">Chief Benefits Guru</div></div>
  <div class="card-band band-orange" style="height:38px"></div>
  <div class="brand" style="left:8px;top:46px;color:#fff"><span class="brand-dot" style="background:var(--paper)"></span>HARBORLINE</div>
</div>

<!-- business card backs -->
<div class="piece card-back" style="left:226px;top:259px">
  <div class="brand"><span class="brand-dot"></span>HARBORLINE</div>
  <div class="services">"Paperless" Open Enrollment<br>Customize a 3-year Benefits Vision<br>Survive a DOL Investigation</div>
</div>
<div class="piece card-back" style="left:226px;top:348px">
  <div class="brand"><span class="brand-dot"></span>HARBORLINE</div>
  <div class="services">"Paperless" Open Enrollment<br>Customize a 3-year Benefits Vision<br>Implement HR Services Portal</div>
</div>
<div class="piece card-back" style="left:226px;top:434px">
  <div class="brand"><span class="brand-dot"></span>HARBORLINE</div>
  <div class="services">Survive a DOL Investigation<br>Customize a 3-year Benefits Vision<br>Implement HR Services Portal</div>
</div>

<!-- letterhead -->
<div class="piece letterhead">
  <div class="brand"><span class="brand-dot"></span>HARBORLINE WORKFORCE</div>
  <div class="faint-mark" role="img" aria-label="Faint circular brand backdrop"></div>
  <div class="lh-footer">Suite 410 27 Kestrel Lane Alderton, NY 13990<br>Phone 555.210.0142 Cell 555.210.0178 Email PMarsh@HarborlineWorkforce.com</div>
  <div class="lh-bar">www.HarborlineWorkforce.com</div>
</div>

<!-- envelope back -->
<div class="piece envelope env-back">
  <div class="brand corner"><span class="brand-dot"></span>HARBORLINE WORKFORCE</div>
  <div class="env-address" style="top:70px">Suite 410 27 Kestrel Lane Alderton, NY 13990<br>Phone 555.210.0142 Cell 555.210.0178 Email PMarsh@HarborlineWorkforce.com</div>
  <div class="env-web" style="top:109px">www.HarborlineWorkforce.com</div>
  <svg class="env-flap" viewBox="0 0 422 157" aria-hidden="true">
    <defs>
      <linearGradient id="flapGrey" x1="0" y1="0" x2="0" y2="1">
        <stop offset="0" stop-color="#aeb1b7"/><stop offset="1" stop-color="#eef0f3"/>
      </linearGradient>
    </defs>
    <path d="M0 0 H422 V40 L211 120 L0 40 Z" fill="url(#flapGrey)"/>
    <path d="M0 40 L211 120 L422 40" fill="none" stroke="#9a9ea6" stroke-width="1"/>
  </svg>
  <div class="env-flap">
    <div class="brand"><span class="brand-dot"></span>HARBORLINE WORKFORCE</div>
  </div>
</div>

<!-- envelope front -->
<div class="piece envelope env-front">
  <div class="brand corner"><span class="brand-dot"></span>HARBORLINE WORKFORCE</div>
  <div class="env-address" style="top:128px">Suite 410 27 Kestrel Lane Alderton, NY 13990<br>Phone 555.210.0142 Cell 555.210.0178 Email PMarsh@HarborlineWorkforce.com</div>
  <div class="env-band" style="top:156px">www.HarborlineWorkforce.com</div>
</div>

</body>
</html>
```